Business Card Design Project

Looking for a logo and business card for a Real State Business i will be opening. The name is not choosen yet , but will probably be RTV IMOVEIS.
I was thinking black and silver colors, but am open to nice ideas.
I did add a business card that i liked a lot, am looking for something like that, with logo in black or silver in a black card. The logo i was thinking in the letters RTV as i uploaded or something or little and cute buildings or a house...just ideas, can be any nice logo.
Updates

You guys can add other colors if you want, I like colors very "BRIGHT" and "open", like red, pink, strong colors. almost glow in the dark colors. lol

Designers,

I've increased more 88 dollars in the budget for 1st place cause I will want envelope designs... small and big sizes.

So 1st place is now U$248,00. 

No need to send the envelope designs right now... only the business cards designs.

Thank you.

Industry/Entity Type

Business

Requirements
Must have
• Renata Tavares Vilela

www.RTVimoveis-exemplo.com.br

+554188316402

renata@rtvimoveis-exemplo.com.br

```html
<!DOCTYPE html>
<html lang="it">
<head>
<meta charset="utf-8">
<title>RTV Imoveis – Stationery</title>
<link rel="stylesheet" href="https://fonts.googleapis.com/css2?family=Open+Sans:wght@400;600&family=Tinos:wght@400;700&display=swap">
<style>
  :root {
    --canvas: #ffffff;
    --paper: #ffffff;
    --paper-edge: #bdbdbd;
    --charcoal: #404042;
    --silver: #cfcfcf;
    --silver-dim: #9a9a9c;
    --ink: #1e1e1e;
    --logo-dark: #4a4a4c;
  }
  * { margin: 0; padding: 0; box-sizing: border-box; }
  html, body { width: 1200px; height: 800px; overflow: hidden; background: var(--canvas); }
  .sheet { position: relative; width: 1200px; height: 800px; }

  .brand-mark {
    font-family: "Open Sans", sans-serif;
    font-weight: 600;
    letter-spacing: -0.02em;
    line-height: 1;
    white-space: nowrap;
  }

  /* Letterhead */
  .letterhead {
    position: absolute; left: 138px; top: 70px; width: 471px; height: 705px;
    background: var(--paper); border: 1px solid var(--paper-edge);
    font-family: "Tinos", serif; color: var(--ink);
  }
  .letterhead .brand-mark { position: absolute; left: 68px; top: 30px; font-size: 24px; color: var(--logo-dark); }
  .letter-body { position: absolute; left: 71px; top: 170px; width: 345px; font-size: 7.4px; line-height: 8.6px; }
  .letter-intro { margin-bottom: 24px; }
  .letter-date { text-align: right; margin-bottom: 40px; }
  .letter-subject { font-weight: 700; margin-bottom: 24px; }
  .letter-salutation { margin-bottom: 8px; }
  .letter-body p.paragraph { margin-bottom: 7px; text-align: justify; }
  .letter-closing { margin-top: 4px; }
  .signature {
    width: 46px; height: 30px; margin: 4px 0 2px 0;
    background: linear-gradient(90deg, #e2e2e2, #cfcfcf);
  }
  .letterhead-url {
    position: absolute; left: 70px; bottom: 16px;
    font-family: "Open Sans", sans-serif; font-size: 6px; color: #666;
    transform: rotate(-90deg); transform-origin: left bottom; white-space: nowrap;
  }

  /* Business cards */
  .card {
    position: absolute; top: 200px; width: 118px; height: 190px;
    background: var(--charcoal); font-family: "Open Sans", sans-serif;
  }
  .card-front { left: 608px; }
  .card-back { left: 738px; }
  .card-contact { position: absolute; left: 15px; top: 72px; font-size: 5.6px; line-height: 7px; }
  .card-name { color: #fff; font-weight: 600; }
  .card-detail { color: var(--silver-dim); }
  .card-rule { width: 12px; height: 1px; background: var(--silver-dim); margin: 8px 0 9px; }
  .card-web { color: #fff; font-weight: 600; }
  .card-back .brand-mark { position: absolute; left: 22px; top: 78px; font-size: 34px; color: var(--silver); }

  /* Envelope */
  .envelope {
    position: absolute; left: 516px; top: 432px; width: 518px; height: 274px;
    background: var(--charcoal);
  }
  .envelope svg { position: absolute; left: 0; top: 0; }
  .envelope-url {
    position: absolute; left: 48px; top: 90px;
    font-family: "Open Sans", sans-serif; font-size: 6.2px; color: var(--silver-dim);
    transform: rotate(-90deg); transform-origin: left top; white-space: nowrap;
  }
  .envelope .brand-mark { position: absolute; left: 46px; top: 135px; font-size: 22px; color: var(--silver); }
</style>
</head>
<body>
<main class="sheet">

  <article class="letterhead">
    <div class="brand-mark">RTV</div>
    <div class="letter-body">
      <p class="letter-intro">Vi invitiamo a leggere<br>questi documenti accuratamente!</p>
      <p class="letter-date">Febbraio 2010</p>
      <p class="letter-subject">Aggiornamento dei dati 2010</p>
      <p class="letter-salutation">Gentili Sigg.re e Sigg.ri,</p>
      <p class="paragraph">Nel quadro dell'aggiornamento annuale della Vostra registrazione nell'Archivio Digitale Nazionale, Vi preghiamo di verificare la correttezza e completezza dei Vostri dati da noi registrati e di rettificarli, se è necessario, sotto il seguente indirizzo Internet: www.archivio-digitale-esempio.it. Solamente così, l'Archivio riporterà i dati più attuali! La Vostra registrazione di base e la sua attualizzazione sono gratuite.</p>
      <p class="paragraph">I Vostri dati attualmente registrati, li troverete nel formulario allegato, che Vi preghiamo di controllare; nel caso in cui volesse passare un ordine soggetto a spese. La registrazione di base gratuita e la sua attualizzazione possono essere effettuate da Voi stessi nel nostro sito www.archivio-digitale-esempio.it sotto il menu, cliccando su „registrazione“.</p>
      <p class="paragraph">Vi auguriamo ancora molto successo con la Vostra registrazione nell'Archivio Digitale Nazionale.</p>
      <p class="letter-closing">Porgiamo distinti saluti</p>
      <div class="signature" role="img" aria-label="Handwritten signature"></div>
      <p>La Vostra redazione</p>
    </div>
    <div class="letterhead-url">www.rtvimoveis-exemplo.com.br</div>
  </article>

  <section class="card card-front">
    <div class="card-contact">
      <div class="card-name">Renata Tavares Vilela</div>
      <div class="card-detail">renata@rtvimoveis-exemplo.com.br</div>
      <div class="card-detail">+55 418 831 6402</div>
      <div class="card-rule"></div>
      <div class="card-web">www.rtvimoveis-exemplo.com.br</div>
    </div>
  </section>

  <section class="card card-back">
    <div class="brand-mark">RTV</div>
  </section>

  <section class="envelope">
    <svg width="518" height="274" viewBox="0 0 518 274" aria-hidden="true">
      <polyline points="1,1 88,108 446,108 517,1" fill="none" stroke="#8a8a8c" stroke-width="0.8"/>
    </svg>
    <div class="envelope-url">www.rtvimoveis-exemplo.com.br</div>
    <div class="brand-mark">RTV</div>
  </section>

</main>
</body>
</html>
```